Fernvale Modern Health Food - Takeaway Menu Design

We are looking for a fresh new takeaway menu that signifies our values: Happy, Healthy, Whole. Fernvale is a modern health food restaurant focusing on locally sourced ingredients where everything is made fresh in house. Menu design will display our menu items and food costs. Will provide logo and list of menu items...
Many items, color pallete, and design ideas can be found on our menu section at www.bimlafernvale.ca
Target Market(s)
Customers and possible catering targets...
Industry/Entity Type
Restaurant
Requirements
Must have
- Logo, menu items with pricing, 2 or 3 fold takeaway design, address, website, phone number

```html
<!DOCTYPE html>
<html lang="en">
<head>
<meta charset="utf-8">
<title>Fernvale Modern Health Food – Smoothies Menu</title>
<link href="https://fonts.googleapis.com/css2?family=Open+Sans:wght@300;400;600;700&family=Josefin+Sans:wght@700&display=swap" rel="stylesheet">
<style>
  :root {
    --teal: #33b7a2;
    --tan: #a48c6c;
    --ink: #2e2e2e;
    --body: #3f3f3f;
    --backdrop: #e8eaeb;
    --paper: #ffffff;
  }
  * { margin: 0; padding: 0; box-sizing: border-box; }
  html, body { width: 1200px; height: 1200px; overflow: hidden; background: var(--backdrop); }
  .menu-page {
    position: absolute; left: 176px; top: 0; width: 848px; height: 1200px;
    background: var(--paper); font-family: "Open Sans", sans-serif; color: var(--body);
  }
  .menu-title {
    position: absolute; left: 0; right: 0; top: 52px; text-align: center;
    font-weight: 700; font-size: 62px; color: var(--teal); letter-spacing: 0.5px; line-height: 1;
  }
  .smoothie { position: absolute; left: 40px; width: 312px; text-align: right; }
  .smoothie-name {
    font-family: "Josefin Sans", sans-serif; font-weight: 700; font-size: 19px;
    color: var(--ink); line-height: 22px; position: relative; text-transform: uppercase;
  }
  .smoothie-price {
    position: absolute; left: 320px; top: 0; color: var(--tan); white-space: nowrap;
  }
  .smoothie-desc { font-size: 16px; line-height: 23px; margin-top: 3px; }
  .photo-stack { position: absolute; left: 438px; top: 160px; width: 370px; height: 340px; }
  .photo-frame {
    position: absolute; inset: 0; background: var(--paper);
    box-shadow: 0 4px 10px rgba(0,0,0,0.28);
  }
  .photo-frame.back { transform: rotate(9deg); }
  .photo-frame.front { transform: rotate(6deg); }
  .photo-fill {
    position: absolute; left: 32px; top: 30px; right: 32px; bottom: 34px;
    background: linear-gradient(135deg, #b49a78 0%, #d8c2a2 40%, #c9ae8a 70%, #8a6a48 100%);
  }
  .story { position: absolute; left: 470px; width: 325px; }
  .story-heading {
    font-family: "Josefin Sans", sans-serif; font-weight: 700; font-size: 16.5px;
    color: var(--teal); text-transform: uppercase; line-height: 20px;
  }
  .story-text { font-size: 15px; line-height: 21px; text-align: justify; margin-top: 2px; letter-spacing: -0.2px; }
  .logo-stack { position: absolute; left: 48px; top: 820px; width: 300px; height: 270px; }
  .logo-card {
    position: absolute; inset: 0; background: var(--paper);
    box-shadow: 0 3px 9px rgba(0,0,0,0.3);
  }
  .logo-card.back { transform: rotate(-2deg) translate(4px, 8px); }
  .logo-card.front { transform: rotate(-5deg); }
  .logo-word {
    position: absolute; left: 0; right: 0; top: 78px; text-align: center;
    font-family: "Open Sans", sans-serif; font-weight: 700; color: var(--teal);
    font-size: 46px; line-height: 1;
  }
  .logo-sub {
    position: absolute; left: 0; right: 0; top: 136px; text-align: center;
    font-family: "Open Sans", sans-serif; font-weight: 700; color: var(--teal);
    font-size: 17px; letter-spacing: 1px; text-transform: uppercase;
  }
  .logo-dot {
    position: absolute; left: 138px; top: 178px; width: 24px; height: 24px;
    border-radius: 50%; background: var(--teal);
  }
  .info-col { position: absolute; top: 1038px; width: 170px; text-align: center; }
  .info-col::before {
    content: ""; display: block; width: 72px; height: 2px; background: var(--teal); margin: 0 auto;
  }
  .info-heading { font-weight: 400; font-size: 20px; color: var(--ink); margin-top: 7px; line-height: 24px; text-transform: uppercase; letter-spacing: -0.5px; }
  .info-lines { font-size: 10.5px; line-height: 15.5px; margin-top: 4px; color: var(--body); }
  .web-band {
    position: absolute; left: 0; bottom: 0; width: 848px; height: 70px; background: var(--teal);
    display: flex; align-items: center; justify-content: center;
    color: var(--paper); font-size: 24px; font-weight: 400;
  }
</style>
</head>
<body>
<main class="menu-page">
  <h1 class="menu-title">SMOOTHIES – 16OZ</h1>

  <section class="smoothie" style="top:158px">
    <h2 class="smoothie-name">Mylkshake<span class="smoothie-price">$6.75</span></h2>
    <p class="smoothie-desc">Almond milk, avocado,<br>banana, vanilla, matcha, dates</p>
  </section>
  <section class="smoothie" style="top:252px">
    <h2 class="smoothie-name">Breakfast<span class="smoothie-price">$6.75</span></h2>
    <p class="smoothie-desc">Mixed berries, banana, spinach,<br>almond milk &amp; coconut water</p>
  </section>
  <section class="smoothie" style="top:345px">
    <h2 class="smoothie-name">Green Protein<span class="smoothie-price">$7.25</span></h2>
    <p class="smoothie-desc">Kale, spinach, lemon,<br>almond meal, avocado, spirulina,<br>honey, vanilla, banana,<br>dates, almond milk</p>
  </section>
  <section class="smoothie" style="top:485px">
    <h2 class="smoothie-name">Frozen Hot Chocolate<span class="smoothie-price">$6.75</span></h2>
    <p class="smoothie-desc">Cacao, macca, dates, cinnamon,<br>avocado, honey, vanilla coconut milk</p>
  </section>
  <section class="smoothie" style="top:579px">
    <h2 class="smoothie-name">Brain Booster<span class="smoothie-price">$6.75</span></h2>
    <p class="smoothie-desc">Carrot juice, blueberries, beet,<br>apple, ginger, lemon, almond milk</p>
  </section>
  <section class="smoothie" style="top:673px">
    <h2 class="smoothie-name">Blueberry Matcha<span class="smoothie-price">$6.75</span></h2>
    <p class="smoothie-desc">Blueberries, banana, dates,<br>matcha, cinnamon, almond milk</p>
  </section>

  <div class="photo-stack">
    <div class="photo-frame back"></div>
    <div class="photo-frame front">
      <div class="photo-fill" role="img" aria-label="Close-up photo of a whole-wheat wrap filled with sprouts and fresh vegetables"></div>
    </div>
  </div>

  <section class="story" style="top:532px">
    <h3 class="story-heading">Our Story</h3>
    <p class="story-text">Food to us is not just something you eat, it is life changing. So it’s time to get back to our roots, in the Kootenay’s where the passion began. It is our mission to serve our community with healthy, whole food working with local businesses whenever possible.</p>
  </section>
  <section class="story" style="top:717px">
    <h3 class="story-heading">Happy, Healthy, and Whole</h3>
    <p class="story-text">Fernvale is a quick-serve restaurant serving food for all diets. All food, sauces, treats, etc. are made in house with the same love that we put into cooking food for our family. We hope to inspire a Happy, Healthy and Whole lifestyle not only through food but also through education; we will be hosting guest speakers to help our community learn more about nutrition, body, mind and soul.</p>
  </section>

  <div class="logo-stack">
    <div class="logo-card back"></div>
    <div class="logo-card front">
      <div class="logo-word">Fernvale</div>
      <div class="logo-sub">Modern Health Food</div>
      <div class="logo-dot"></div>
    </div>
  </div>

  <div class="info-col" style="left:353px">
    <h4 class="info-heading">Location</h4>
    <p class="info-lines">#4 2210 Alder Ave<br>Brennick, BC, V2K 3R8</p>
  </div>
  <div class="info-col" style="left:505px">
    <h4 class="info-heading">Hours</h4>
    <p class="info-lines">Monday to Friday – 8am to 7pm<br>Saturday – 9am to 5pm<br>Sunday – Closed</p>
  </div>
  <div class="info-col" style="left:655px">
    <h4 class="info-heading">Contact</h4>
    <p class="info-lines">Phone: 250-555-0187<br>Email: info@bimlafernvale.ca</p>
  </div>

  <footer class="web-band">www.bimlafernvale.ca</footer>
</main>
</body>
</html>
```